Quilvo Garage Doors Business Card

I need a Business Card for my garage door business:
Quilvo Garage Doors.
please add:
logo
phone number: 855-3-QUILVO
(853-392)

email: service@quilvogaragedoors.com
website: www.quilvogaragedoors.com

The attached image is recommendation ONLY.

```html
<!DOCTYPE html>
<html lang="en">
<head>
<meta charset="UTF-8">
<title>Quilvo Garage Doors – Business Card</title>
<link rel="stylesheet" href="https://fonts.googleapis.com/css2?family=Arimo:wght@700&display=swap">
<style>
  :root {
    --teal: #58c3cf;
    --ink: #221f20;
    --deep: #03161b;
    --paper: #ffffff;
  }
  * { margin: 0; padding: 0; box-sizing: border-box; }
  html, body { width: 1050px; height: 1200px; overflow: hidden; background: var(--paper); }
  .card {
    position: relative;
    width: 1050px;
    height: 1200px;
    background: var(--paper);
    font-family: "Arimo", Arial, sans-serif;
    color: var(--ink);
  }
  .card__band {
    position: absolute;
    left: 0; top: 0;
    width: 1050px; height: 600px;
    background: var(--teal);
  }
  .card__band-mark {
    position: absolute;
    left: 743px; top: 310px;
    width: 260px; height: 260px;
    border-radius: 50%;
    background: var(--deep);
  }
  .card__emblem {
    position: absolute;
    left: 50px; top: 765px;
    width: 290px; height: 290px;
    border-radius: 50%;
    background: var(--teal);
  }
  .card__divider {
    position: absolute;
    left: 386px; top: 648px;
    width: 4px; height: 534px;
    background: var(--teal);
  }
  .brand {
    position: absolute;
    left: 500px; top: 640px;
    font-weight: 700;
    font-size: 70px;
    line-height: 84px;
    color: var(--ink);
  }
  .contact {
    position: absolute;
    right: 14px; top: 860px;
    list-style: none;
    text-align: right;
  }
  .contact__item {
    display: flex;
    justify-content: flex-end;
    align-items: center;
    gap: 18px;
    font-weight: 700;
    font-size: 31px;
    height: 80px;
  }
  .contact__item--name { font-size: 50px; height: 80px; }
  .contact__bullet { width: 22px; height: 24px; flex: none; }
  .contact__bullet polygon { fill: var(--teal); }
</style>
</head>
<body>
  <div class="card">
    <div class="card__band">
      <div class="card__band-mark"></div>
    </div>

    <div class="card__emblem"></div>
    <div class="card__divider"></div>

    <div class="brand">Quilvo<br>Garage Doors</div>

    <ul class="contact">
      <li class="contact__item contact__item--name">Dana Morrow
        <svg class="contact__bullet" viewBox="0 0 22 24"><polygon points="11,0 22,6 22,18 11,24 0,18 0,6"/></svg>
      </li>
      <li class="contact__item">855-3-QUILVO
        <svg class="contact__bullet" viewBox="0 0 22 24"><polygon points="11,0 22,6 22,18 11,24 0,18 0,6"/></svg>
      </li>
      <li class="contact__item">service@quilvogaragedoors.com
        <svg class="contact__bullet" viewBox="0 0 22 24"><polygon points="11,0 22,6 22,18 11,24 0,18 0,6"/></svg>
      </li>
      <li class="contact__item">www.quilvogaragedoors.com
        <svg class="contact__bullet" viewBox="0 0 22 24"><polygon points="11,0 22,6 22,18 11,24 0,18 0,6"/></svg>
      </li>
    </ul>
  </div>
</body>
</html>
```